Buch-/E-Book-Cover für SEO Experte
Zielgruppe
SEO Experte Lorenz K. Abendroth ist Geschäftsführer einer SEO Agentur in Köln und bringt nun 'Das dicke Netzsuche & Webwerbung Handbuch' auf den Markt. ein kompaktes Werk welches alle Begrifflichkeiten und Konzepte aus der Welt der SEO Optimierung und des Online Marketings einfach erläutert zum nachschlagen in typischer Lexikon Manier.
Titel: Das dicke Netzsuche & Webwerbung Handbuch
Subtitel: Alle Fragen & Begriffe aus 6 Jahren SEO Agenturarbeit einfach erklärt und kompakt zusammengefasst zum nachschlagen
Aufgabenstellung
Es soll anders sein als das dazugehörige komplementär Buch 'Pixelhaus Ranking 2031' aber dennoch im selben Stil gearbeitet sein. Es soll wie ein sehr wertiges großes altes Lexikon wirken mit vielen Seiten. Bitte auch ein stehendes 3D Cover zum normalen Druck Cover liefern.

```html
<!DOCTYPE html>
<html lang="de">
<head>
<meta charset="utf-8">
<title>Das dicke Netzsuche &amp; Webwerbung Handbuch – Umschlag</title>
<link href="https://fonts.googleapis.com/css2?family=Open+Sans:wght@300;400;700;800&family=Oswald:wght@300;400;600&family=Yanone+Kaffeesatz:wght@400;700&family=Montserrat:wght@400;700&display=swap" rel="stylesheet">
<style>
  :root {
    --teal: #27c9ad;
    --teal-deep: #1fae96;
    --white: #ffffff;
    --band: #f2f2f2;
    --ink: #333333;
    --ink-soft: #555555;
  }
  * { margin: 0; padding: 0; box-sizing: border-box; }
  html, body { width: 1200px; height: 560px; overflow: hidden; background: var(--white); }
  .cover { position: relative; width: 1200px; height: 560px; background: var(--teal); overflow: hidden; font-family: "Open Sans", sans-serif; color: var(--white); }
  .bottom-band { position: absolute; left: 0; top: 479px; width: 1200px; height: 81px; background: var(--band); }

  /* back */
  .back-headline { position: absolute; left: 257px; top: 46px; font-size: 20px; line-height: 25px; font-weight: 400; }
  .back-headline strong { display: block; font-size: 23px; font-weight: 800; }
  .back-copy { position: absolute; left: 257px; width: 300px; font-size: 9.6px; line-height: 13.4px; font-weight: 400; }
  .back-copy strong { font-weight: 700; }
  .copy-one { top: 121px; }
  .copy-two { top: 194px; }
  .learn-label { position: absolute; left: 258px; top: 244px; font-size: 10.5px; font-weight: 700; }
  .placeholder-box { position: absolute; left: 258px; top: 261px; width: 254px; height: 97px; background: var(--white); color: var(--ink); display: flex; flex-direction: column; justify-content: center; align-items: center; font-weight: 700; font-size: 21px; line-height: 25px; text-align: center; }
  .author-card { position: absolute; left: 257px; top: 370px; width: 280px; height: 79px; background: linear-gradient(90deg, #f4f4f4, #e8e8e8); display: flex; box-shadow: 0 2px 6px rgba(0,0,0,.25); }
  .author-photo { width: 70px; height: 79px; background: linear-gradient(135deg, #c9c9c9, #8a8a8a 60%, #2e3440); }
  .author-bio { flex: 1; padding: 8px 6px 0 10px; font-family: "Montserrat", sans-serif; font-size: 8.3px; line-height: 10.2px; color: var(--ink); }
  .author-bio strong { font-weight: 700; }
  .known-label { position: absolute; left: 292px; top: 489px; width: 200px; text-align: center; font-size: 8.5px; font-weight: 700; color: var(--ink-soft); }
  .partner-row { position: absolute; left: 228px; top: 514px; width: 335px; display: flex; justify-content: space-between; align-items: center; }
  .partner { display: flex; align-items: center; gap: 3px; font-size: 7px; font-weight: 700; color: var(--ink-soft); white-space: nowrap; }
  .partner i { display: block; width: 10px; height: 10px; background: #6a6a6a; flex: none; }
  .partner i.round { border-radius: 50%; }

  /* spine */
  .spine-title { position: absolute; left: 590px; top: 41px; height: 268px; writing-mode: vertical-rl; font-family: "Oswald", sans-serif; font-weight: 600; font-size: 16px; line-height: 20px; letter-spacing: 0.3px; white-space: nowrap; text-align: center; }
  .spine-tag { position: absolute; left: 594px; top: 326px; width: 14px; height: 134px; border: 1px solid var(--white); writing-mode: vertical-rl; font-size: 7.2px; line-height: 12px; text-align: center; white-space: nowrap; }
  .spine-author { position: absolute; left: 592px; top: 484px; writing-mode: vertical-rl; font-size: 7.5px; line-height: 9px; color: var(--ink-soft); text-transform: uppercase; }

  /* front */
  .new-tab { position: absolute; left: 636px; top: 0; width: 78px; height: 25px; }
  .new-tab span { position: absolute; left: 0; top: 2px; width: 78px; text-align: center; font-weight: 800; font-size: 16px; color: var(--teal); }
  .front-title { position: absolute; left: 620px; top: 42px; width: 383px; text-align: center; font-family: "Oswald", sans-serif; font-weight: 400; font-size: 33px; line-height: 42px; text-transform: uppercase; }
  .front-title strong { font-weight: 600; }
  .subtitle-box { position: absolute; left: 630px; top: 198px; width: 354px; height: 69px; border: 1px solid var(--white); display: flex; align-items: center; justify-content: center; text-align: center; font-family: "Yanone Kaffeesatz", sans-serif; font-size: 19px; line-height: 18px; }
  .subtitle-box strong { font-weight: 700; }
  .front-artwork { position: absolute; left: 682px; top: 296px; width: 248px; height: 206px; }
  .front-author { position: absolute; left: 620px; top: 521px; width: 383px; text-align: center; font-size: 10px; font-weight: 300; color: var(--ink); text-transform: uppercase; }
</style>
</head>
<body>
<main class="cover">
  <div class="bottom-band"></div>

  <section class="back">
    <h2 class="back-headline">Nehmen Sie ihren SEO-Erfolg <strong>jetzt selbst in die Hand!</strong></h2>
    <p class="back-copy copy-one">Der <strong>Erfahrungsschatz</strong> aus über 6 Jahren hauptberuflicher SEO-Optimierung für SeitenWerk kompakt und gut aufbereitet zusammengefasst. Sie erhalten das komplette Rüstzeug, mit dem mein Team und ich in den letzten Jahren <strong>überragende SEO-Erfolge</strong> für unsere Kunden erzielt haben.</p>
    <p class="back-copy copy-two">Alle <strong>Fragen &amp; Begriffe</strong> aus <strong>6 Jahren</strong> SEO Agenturarbeit werden Ihnen hier einfach erklärt und kompakt zusammengefasst und das alles zum praktischen nachschlagen.</p>
    <p class="learn-label">Sie werden u.a lernen:</p>
    <div class="placeholder-box"><span>PLATZHALTER</span><span>(Inhalt des Lexikons)</span></div>
    <div class="author-card">
      <div class="author-photo" role="img" aria-label="Porträtfoto des Autors"></div>
      <p class="author-bio"><strong>Lorenz K. Abendroth</strong> ist Geschäftsführer einer Kölner SEO-Agentur und arbeitete bereits als <strong>Suchportal-Trainer</strong>, Kammer-Referent, Digital Marketing Berater und als Dozent für Suchmaschinenoptimierung am Kolleg für Medien in Köln.</p>
    </div>
    <p class="known-label">Bekannt aus / Veröffentlicht bei:</p>
    <div class="partner-row">
      <span class="partner"><i class="round"></i>Rankwerk</span>
      <span class="partner"><i></i>Werkbund Rhein</span>
      <span class="partner"><i></i>Kammer Rhein</span>
      <span class="partner"><i></i>Netzwachstum</span>
      <span class="partner">Medienkolleg</span>
      <span class="partner"><i></i>Suchtreff</span>
    </div>
  </section>

  <section class="spine">
    <p class="spine-title">NETZSUCHE &amp; WEBWERBUNG HANDBUCH</p>
    <p class="spine-tag">6 Jahre SEO Agenturarbeit erklärt</p>
    <p class="spine-author">Lorenz<br>Abendroth</p>
  </section>

  <section class="front">
    <div class="new-tab">
      <svg width="78" height="25" viewBox="0 0 78 25"><polygon points="6,0 78,0 72,25 0,25" fill="#ffffff"/></svg>
      <span>NEU!</span>
    </div>
    <h1 class="front-title">Das <strong>dicke</strong><br>Netzsuche &amp;<br>Webwerbung Handbuch</h1>
    <div class="subtitle-box"><p>Alle Fragen &amp; Begriffe aus <strong>6 Jahren</strong><br>SEO Agenturarbeit einfach erklärt und kompakt<br>zusammengefasst zum nachschlagen</p></div>
    <svg class="front-artwork" viewBox="0 0 248 206" role="img" aria-label="Illustration eines Laptops mit Lupe und Suchleiste auf hellem Sockel">
      <defs>
        <radialGradient id="artGlow" cx="50%" cy="55%" r="55%">
          <stop offset="0%" stop-color="#e8f7f3"/>
          <stop offset="100%" stop-color="#27c9ad" stop-opacity="0"/>
        </radialGradient>
      </defs>
      <ellipse cx="124" cy="110" rx="124" ry="96" fill="url(#artGlow)"/>
    </svg>
    <p class="front-author">Lorenz Kasimir Abendroth</p>
  </section>
</main>
</body>
</html>
```